Computer repair services flyer

This flyer / leaflet is required to promote my local computer and laptop repair business. It will primarily be used for pinning to notice boards when I get access to shared accommodation but I will also use it in the future for posting through letterboxes in affluent areas.

Company branding, logo, services, pricing, contact details etc. can be found on my website at : www.brightlanetech.co.uk

The services I would predominantly like to promote on this flyer are :

Speeding up slow / old computers
Virus removal
Lost data recovered
Broken laptop screen replacements
Dead laptops fixed
We buy and recycle broken laptops for cash

Other features to highlight :

Friendly and experienced
We are local (Near to Cardiff city center)
Quick repair turnaround - most repairs within 24hours
Affordable / No VAT
Free diagnostics
No Fix = No fee
Free collection and delivery
We Guarantee our work

Calls to action and attention grabbing if possible. Offer 10% off. Free cooling fan clean.

Size of flyer = A5 (210 x 148mm or 8.3 x 5.8in) portrait, single sided colour.

Target Market(s)

18 to 60 years

Industry/Entity Type

Accommodation

Requirements
Must have
• 02940 613857

```html
<!DOCTYPE html>
<html lang="en">
<head>
<meta charset="utf-8">
<title>Bright Lane Tech – Computer Repair Flyer</title>
<link rel="stylesheet" href="https://fonts.googleapis.com/css2?family=Arimo:wght@400;700&family=Roboto+Condensed:wght@700&display=swap">
<style>
  :root {
    --orange: #f26522;
    --black: #131313;
    --white: #ffffff;
    --ink: #1e1e1e;
    --grey: #555555;
  }
  * { margin: 0; padding: 0; box-sizing: border-box; }
  html, body { width: 845px; height: 1200px; overflow: hidden; background: var(--white); }
  .flyer {
    position: relative; width: 845px; height: 1200px; overflow: hidden;
    font-family: "Arimo", Arial, sans-serif; color: var(--ink); background: var(--white);
  }
  .photo-team {
    position: absolute; left: 0; top: 0; width: 425px; height: 285px;
    background: linear-gradient(160deg, #c9d3dc 0%, #8595a6 45%, #2f3a48 100%);
  }
  .photo-tech {
    position: absolute; left: 425px; top: 0; width: 420px; height: 255px;
    background: linear-gradient(135deg, #f3f6fa 0%, #a9c1da 45%, #3f6a9a 100%);
  }
  .brand {
    position: absolute; left: 0; top: 285px; width: 425px; height: 220px;
    display: flex; align-items: center; gap: 14px; padding-left: 30px;
  }
  .brand-mark { width: 28px; height: 28px; background: var(--orange); flex: none; }
  .brand-name { font-size: 38px; font-weight: 700; color: var(--black); line-height: 1; white-space: nowrap; }

  .call {
    position: absolute; left: 425px; top: 255px; width: 420px; height: 215px;
    background: var(--orange); color: var(--white); padding: 40px 0 0 36px;
  }
  .call-label { font-size: 56px; font-weight: 700; line-height: 1; white-space: nowrap; }
  .call-number { font-size: 54px; font-weight: 700; line-height: 1.2; margin-top: 14px; white-space: nowrap; }

  .services {
    position: absolute; left: 425px; top: 470px; width: 420px; height: 575px;
    background: var(--black); color: var(--white);
  }
  .services-title {
    position: absolute; left: 4px; top: 0; width: 64px; height: 450px;
    display: flex; align-items: center; justify-content: center;
  }
  .services-title span {
    transform: rotate(-90deg); white-space: nowrap; color: var(--orange);
    font-family: "Roboto Condensed", "Arial Narrow", sans-serif; font-size: 50px; font-weight: 700;
  }
  .service-list { position: absolute; left: 78px; top: 26px; right: 16px; list-style: none; }
  .service-list li {
    position: relative; padding-left: 30px; margin-bottom: 20px;
    font-family: "Roboto Condensed", "Arial Narrow", sans-serif; font-size: 29px; font-weight: 700; line-height: 1.15;
  }
  .service-list li::before {
    content: ""; position: absolute; left: 0; top: 10px; width: 14px; height: 14px; background: var(--orange);
  }
  .price {
    position: absolute; left: 78px; top: 462px; display: flex; align-items: flex-end; gap: 16px;
    color: var(--orange); font-weight: 700; white-space: nowrap;
  }
  .price-label { font-family: "Roboto Condensed", "Arial Narrow", sans-serif; font-size: 38px; line-height: 1; }
  .price-value { font-size: 80px; line-height: 0.9; }

  .features { position: absolute; left: 26px; top: 518px; width: 390px; list-style: none; }
  .features li {
    position: relative; padding-left: 40px; margin-bottom: 12px;
    font-size: 25px; font-weight: 700; line-height: 1.2; color: var(--ink);
  }
  .features li svg { position: absolute; left: 0; top: 4px; width: 26px; height: 24px; }

  .offer-band {
    position: absolute; left: 0; top: 1050px; width: 845px; height: 46px;
    background: var(--orange); color: var(--white);
    display: flex; align-items: center; justify-content: center;
    font-family: "Roboto Condensed", "Arial Narrow", sans-serif; font-size: 19px; font-weight: 700; white-space: nowrap;
  }
  .map {
    position: absolute; left: 0; top: 1096px; width: 280px; height: 104px;
    background: linear-gradient(120deg, #e6eadf 0%, #cfd8c4 50%, #b9c7d6 100%);
  }
  .contact { position: absolute; left: 300px; top: 1104px; width: 290px; font-size: 15px; line-height: 1.25; }
  .contact p { display: flex; align-items: center; gap: 8px; white-space: nowrap; }
  .contact svg { width: 15px; height: 15px; flex: none; }
  .contact .address { padding-left: 23px; position: relative; display: block; }
  .contact .address svg { position: absolute; left: 0; top: 2px; }
  .social { position: absolute; left: 600px; top: 1104px; list-style: none; }
  .social li { display: flex; align-items: center; gap: 10px; font-size: 15px; margin-bottom: 4px; height: 20px; white-space: nowrap; }
  .social li::before { content: ""; width: 18px; height: 18px; background: var(--orange); flex: none; }
</style>
</head>
<body>
<div class="flyer">
  <div class="photo-team" role="img" aria-label="Photo of a smiling repair team giving thumbs up"></div>
  <div class="photo-tech" role="img" aria-label="Photo of a keyboard with a stethoscope"></div>

  <div class="brand">
    <span class="brand-mark"></span>
    <span class="brand-name">Bright Lane Tech</span>
  </div>

  <div class="call">
    <p class="call-label">Call Now</p>
    <p class="call-number">02940 613857</p>
  </div>

  <ul class="features">
    <li><svg viewBox="0 0 26 24"><path d="M2 13l7 7L24 3" fill="none" stroke="#f26522" stroke-width="5"/></svg>Friendly and experienced</li>
    <li><svg viewBox="0 0 26 24"><path d="M2 13l7 7L24 3" fill="none" stroke="#f26522" stroke-width="5"/></svg>We are local (Near to Cardiff city center)</li>
    <li><svg viewBox="0 0 26 24"><path d="M2 13l7 7L24 3" fill="none" stroke="#f26522" stroke-width="5"/></svg>Quick repair turnaround - most repairs within 24hours</li>
    <li><svg viewBox="0 0 26 24"><path d="M2 13l7 7L24 3" fill="none" stroke="#f26522" stroke-width="5"/></svg>Affordable / No VAT</li>
    <li><svg viewBox="0 0 26 24"><path d="M2 13l7 7L24 3" fill="none" stroke="#f26522" stroke-width="5"/></svg>Free diagnostics</li>
    <li><svg viewBox="0 0 26 24"><path d="M2 13l7 7L24 3" fill="none" stroke="#f26522" stroke-width="5"/></svg>No Fix = No Fees</li>
    <li><svg viewBox="0 0 26 24"><path d="M2 13l7 7L24 3" fill="none" stroke="#f26522" stroke-width="5"/></svg>Free collection and delivery</li>
    <li><svg viewBox="0 0 26 24"><path d="M2 13l7 7L24 3" fill="none" stroke="#f26522" stroke-width="5"/></svg>We Guarantee our work</li>
  </ul>

  <section class="services">
    <div class="services-title"><span>OUR SERVICES</span></div>
    <ul class="service-list">
      <li>Speeding up slow / old computers</li>
      <li>Virus removal</li>
      <li>Lost data recovered</li>
      <li>Broken laptop screen replacements</li>
      <li>Dead laptops fixed</li>
      <li>We buy and recycle broken laptops for cash</li>
    </ul>
    <div class="price">
      <span class="price-label">Prices<br>start from</span>
      <span class="price-value">£19</span>
    </div>
  </section>

  <div class="offer-band">Calls to action and attention grabbing if possible. Offer 10% off. Free cooling fan clean.</div>

  <div class="map" role="img" aria-label="Street map of Cardiff"></div>

  <div class="contact">
    <p class="address"><svg viewBox="0 0 16 16"><path d="M8 1a5 5 0 0 0-5 5c0 4 5 9 5 9s5-5 5-9a5 5 0 0 0-5-5zm0 7a2 2 0 1 1 0-4 2 2 0 0 1 0 4z" fill="#f26522"/></svg>14 Harlow Street,<br>Llanishen<br>Cardiff&nbsp; CF14 2QT</p>
    <p><svg viewBox="0 0 16 16"><rect x="1" y="3" width="14" height="10" fill="#f26522"/><path d="M1 3l7 6 7-6" fill="none" stroke="#fff" stroke-width="1.5"/></svg>hello@brightlanetech.co.uk</p>
    <p><svg viewBox="0 0 16 16"><circle cx="8" cy="8" r="7" fill="#f26522"/></svg>www. brightlanetech.co.uk</p>
  </div>

  <ul class="social">
    <li>brightlanetech.co.uk</li>
    <li>brightlanetech.co.uk</li>
    <li>brightlanetech.co.uk</li>
    <li>brightlanetech.co.uk</li>
  </ul>
</div>
</body>
</html>
```